Speisekarte für Pizzeria
Zielgruppe
Hallo in die Runde,
Wir würden gerne für unser Restaurant / Pizzeria eine neue Speisekarte haben.
Wir sind im höchsten Skigebiet Österreichs umgeben von Bergen und Schnee
am besten könnte ich es euch vorstellen bei einer Drohnen-Aufnahme die ihr unter folgendem Link sehen könnt:
www.firnblick.ag/panorama
Aufgabenstellung
Wir würden gerne ein quadratisches Format haben - 300x300mm
Der Druck sollte auf www.presswerk.at erfolgen
4 Umschlagseiten und 4 Kernseiten
Als Anhang hab ich euch meine jetzige Speisekarte drangehängt...diese ist lediglich im A4 Format und einfach eine klassische Speisekarte.
Nachtrag: weil da einige Fragen aufgekommen sind: die neue Karte sollte alle Speisen sowie auch alle Pizze und Getränke enthalten. Und auf der letzte Seite sollte irgendwie Werbung für unsere Appartments und unseren Wellness-Bereich gemacht werden. Foto gibt es unter www.almrosen.at ... wenn wir dann beim Finalisieren sind, kann ich die Fotos gerne in guter Qualität nachreichen
Wir haben bei uns im Haus auch Appartments mit Wellness Bereich und diese Gäste kommen natürlich auch ins Restaurnt. Weiters kommen aber natürlich auch Gäste aus anderen umliegenden Hotels / Betrieben...um diesen Gästen einen Anreiz zu schaffen, in Zukunft bei uns ihren Urlaub zu verbringen, würde ich gerne auf der letzten Seite unser Hotel bewerben...vielleicht mit einigen Fotos vom Schwimmbad / Ruheraum etc.
Wir haben hier auf dieser Plattform bereits einmal erfolgreich unsere Pizzakartons machen lassen... ein Foto von diesen habe ich auch drangehängt...aber das Design zu übernehmen ist kein Muss !
In unserer jetzigen Speisekarte sind nicht alle Spirituosen angeführt...dort sollte man vielleicht etwas mehr Platz einrechnen, damit ich alle Longdrinks etc. anführen kann. Dies würde ich dann aber erst gerne nachreichen wenn wir mal ein Design haben.

```html
<!DOCTYPE html>
<html lang="de">
<head>
<meta charset="utf-8">
<title>Toni's – Speisekarte</title>
<link href="https://fonts.googleapis.com/css2?family=Oswald:wght@300;400&family=Playfair+Display:ital,wght@0,400;0,700;1,400&display=swap" rel="stylesheet">
<style>
:root{
  --backdrop:#a7a7a7;
  --slate:#2a2a2a;
  --slate-light:#353535;
  --gold:#f3d21c;
  --ink:#e9e9e9;
  --muted:#bdbdbd;
}
*{margin:0;padding:0;box-sizing:border-box}
html,body{width:1200px;height:3514px;overflow:hidden;background:var(--backdrop)}
body{position:relative;font-family:"Playfair Display",serif}
.page{position:absolute;width:540px;height:540px;overflow:hidden;
  background:radial-gradient(circle at 30% 25%,var(--slate-light),var(--slate) 60%,#222 100%);}
.bracket{position:absolute;left:36px;top:30px;width:110px;height:80px;border-left:1px solid #6d6a55;border-top:1px solid #6d6a55}
.bracket::before{content:"";position:absolute;left:-9px;top:-9px;width:14px;height:14px;border:1px solid var(--muted);border-radius:50%;background:var(--slate)}
.footline{position:absolute;left:36px;right:36px;bottom:28px;border-top:1px solid #6a6233}
.folio{position:absolute;left:0;right:0;bottom:18px;text-align:center;font-size:7px;color:var(--gold)}
.title{position:absolute;border:1px solid #8a7d2a;padding:4px 8px;font-family:Oswald,sans-serif;font-weight:300;font-size:28px;color:var(--ink);letter-spacing:.3px;line-height:1.15;white-space:nowrap}
.title small{font-size:20px}
.art{position:absolute;border-radius:50%;background:radial-gradient(circle,rgba(243,210,28,.55),rgba(243,210,28,.12) 65%,transparent 72%)}
.art.square{border-radius:6px}
.menu{position:absolute;list-style:none}
.menu li{display:grid;grid-template-columns:1fr auto;column-gap:14px;margin-bottom:9px}
.menu h3{grid-column:1/3;font-size:8.5px;font-weight:700;color:var(--gold);line-height:1.25}
.menu p{font-size:6.5px;color:var(--ink);line-height:1.35;letter-spacing:.2px}
.menu .price{font-size:6.5px;color:var(--ink);align-self:end;white-space:nowrap;text-align:right}
.wordmark{position:absolute;left:0;right:0;text-align:center;font-family:Oswald,sans-serif;font-weight:400;color:var(--gold);letter-spacing:2px}
.wordmark::before{content:"";display:block;margin:0 auto 6px;width:14px;height:14px;border-radius:50%;background:var(--gold)}
.photo{position:absolute;background:linear-gradient(135deg,#c9b79b,#8f7a5f 55%,#5e4c3a)}
.team{position:absolute;left:158px;top:50px;font-family:Oswald,sans-serif;font-size:16px;color:var(--gold)}
.welcome{position:absolute;left:207px;top:82px;font-size:7px;font-style:italic;color:var(--gold);line-height:1.5}
.contact{position:absolute;left:0;right:0;top:284px;text-align:center;font-family:Oswald,sans-serif;font-size:12px;color:var(--gold);line-height:2.1;letter-spacing:.5px}
.vertical-note{position:absolute;left:72px;bottom:60px;transform:rotate(-90deg);transform-origin:left bottom;font-size:5.5px;color:var(--muted);white-space:nowrap}
</style>
</head>
<body>

<section class="page cover" style="left:615px;top:39px">
  <div class="wordmark" style="top:105px;font-size:46px">TONI'S</div>
  <div class="art" role="img" aria-label="Gezeichnete Pizza mit herausgeschnittenem Stück in Gelb" style="left:-60px;top:250px;width:370px;height:330px"></div>
  <div class="art" role="img" aria-label="Gezeichnete Pilze, Oliven und Tomatenscheibe" style="left:320px;top:330px;width:170px;height:140px"></div>
  <div class="art" role="img" aria-label="Gezeichnetes Basilikumblatt" style="left:460px;top:300px;width:50px;height:60px"></div>
</section>

<section class="page" style="left:39px;top:601px">
  <div class="bracket"></div>
  <div class="team">TONI'S TEAM</div>
  <p class="welcome">heisst Sie herzlich Willkommen und<br>&nbsp;&nbsp;&nbsp;&nbsp;&nbsp;&nbsp;&nbsp;&nbsp;&nbsp;&nbsp;wünscht Ihnen einen guten Appetit !</p>
  <div class="title" style="left:204px;top:165px">VORSPEISEN</div>
  <ul class="menu" style="left:120px;top:232px;width:320px">
    <li><h3>Carpaccio vom Tiroler Weiderind</h3><p>Trüffelcreme, Parmesanspäne, hausgemachtes Brot</p><span class="price">€ 16,90</span></li>
    <li><h3>Tartar von der Roten Beete &amp; Avocado</h3><p>mit Wakame Alge, Wasabi-Schaum und hausgemachtem Brot</p><span class="price">€ 14,90</span></li>
    <li><h3>Vitello Tonnato</h3><p>rosa Kalbsfleisch Scheiben, Thunfischcreme,<br>Rucola, Tomaten, Pesto, Kapern, hausgemachtes Brot</p><span class="price">€ 16,50</span></li>
  </ul>
  <ul class="menu" style="left:120px;top:372px;width:320px">
    <li><h3>Zu allen Salaten empfehlen wir:</h3><p>Knoblauchbaguette mit hausgemachter Butter<br>Knoblauchbrot<br>Pizzabrot</p><span class="price">€ 4,50<br>€ 3,90<br>€ 3,50</span></li>
  </ul>
  <div class="art" role="img" aria-label="Gezeichnete Oliven" style="left:20px;top:160px;width:60px;height:90px"></div>
  <div class="art" role="img" aria-label="Gezeichnete Knoblauchknolle und Rosmarinzweig" style="left:-20px;top:330px;width:170px;height:150px"></div>
  <div class="footline"></div><div class="folio">- 2 -</div>
</section>

<section class="page" style="left:613px;top:598px">
  <div class="title" style="left:215px;top:42px">SUPPEN</div>
  <ul class="menu" style="left:108px;top:98px;width:330px">
    <li><h3>Tomatencremesuppe</h3><p>Basilikum / Croutons (auch vegan möglich)</p><span class="price">€ 7,50</span></li>
    <li><h3>Kartoffel-Zwiebelsuppe</h3><p>im Topf serviert mit Käse-Croutons</p><span class="price">€ 8,50</span></li>
    <li><h3>Rindsuppe mit Kräuter-Frittaten</h3><p></p><span class="price">€ 6,90</span></li>
  </ul>
  <div class="title" style="left:220px;top:188px">SALATE</div>
  <ul class="menu" style="left:108px;top:248px;width:330px">
    <li><h3>gemischter Salat</h3><p></p><span class="price">€ 6,90</span></li>
    <li><h3>Cesar Salat</h3><p>• Das Original / Parmesanspäne / Croutons ohne Beilage<br>• mit gegrilltem Hühnerbrust<br>• mit Knoblauch-Garnelen</p><span class="price">€ 11,90<br>€ 15,90<br>€ 18,90</span></li>
    <li><h3>Winter - Bowl</h3><p>Blattsalate / Granatapfelkerne / Schafskäse / Kirschtomaten<br>Bulgur / Parmesanchips / Pinienkerne / rote Zwiebel / Gurken</p><span class="price">€ 15,90</span></li>
  </ul>
  <div class="art" role="img" aria-label="Gezeichnete Tomatenscheibe, Pilz und Oliven" style="left:200px;top:390px;width:150px;height:100px"></div>
  <div class="footline"></div><div class="folio">- 3 -</div>
</section>

<section class="page" style="left:39px;top:1158px">
  <div class="bracket"></div>
  <div class="art" role="img" aria-label="Gezeichnete Peperoni" style="left:150px;top:18px;width:100px;height:60px"></div>
  <div class="title" style="left:150px;top:100px">PASTA / FISCH &amp; MEHR</div>
  <ul class="menu" style="left:120px;top:158px;width:350px">
    <li><h3>Hausgemachte Schlutzkrapfen</h3><p>Topfenschaum gefüllt mit Topfen &amp; Spinat<br>serviert mit Parmesan &amp; brauner Butter</p><span class="price">5 Stück € 11,90<br>8 Stück € 16,90</span></li>
    <li><h3>Spaghetti al Chef</h3><p>Garnelen / Kirschtomaten / Peperoncino / Knoblauch<br>Kräuter / Olivenöl</p><span class="price">€ 17,90</span></li>
    <li><h3>Spaghetti Pesto</h3><p>Basilikum / Knoblauch / Olivenöl / Pinienkerne / Parmesan</p><span class="price">€ 13,90</span></li>
    <li><h3>Spaghetti Bolognese</h3><p></p><span class="price">€ 12,90</span></li>
    <li><h3>Seeblingfilet</h3><p>Kross gebraten aus Tiroler Gewässern<br>Tagliatelle / Fenchel / Lauch / Zitrone<br>Spinatblätter / Tomatenflocken</p><span class="price">€ 21,90</span></li>
    <li><h3>Carpaccio mit Trüffel-Spaghettini</h3><p>ein original italienisches Rezept verfeinert mit Rucola &amp; Parmesan</p><span class="price">€ 20,90</span></li>
  </ul>
  <div class="art" role="img" aria-label="Gezeichneter Fisch" style="left:-20px;top:400px;width:190px;height:110px"></div>
  <div class="footline"></div><div class="folio">- 4 -</div>
</section>

<section class="page" style="left:617px;top:1161px">
  <div class="title" style="left:122px;top:82px"><small>AUS DEM </small>HOLZKOHLEGRILL</div>
  <ul class="menu" style="left:105px;top:142px;width:345px">
    <li><h3>bei offenem Feuer und 350°</h3><p>Alle drei serviert wir mit<br>Gemüse / Pommes frites / 2 kalte Saucen / Kräuterbutter</p><span class="price"></span></li>
    <li><h3>Filetsteak</h3><p></p><span class="price">ca. 200g € 33,90</span></li>
    <li><h3>Saftige hausgemachte Rippchen</h3><p>Vom rohe gegart und im Grill verfeinert<br>am Brett serviert / 2 Saucen / Folienkartoffel mit Dip<br>und Knoblauchbaguette</p><span class="price">€ 28,90</span></li>
    <li><h3>Tagliata</h3><p>ca. 250g vom Rumpsteak<br>in Streifen geschnitten dazu Rucola<br>Kirschtomaten / Parmesan / Knoblauchöl</p><span class="price">€ 26,90</span></li>
    <li><h3>Holzfällersteak</h3><p>vom Schweinerücken<br>Speck / Zwiebel / Bier</p><span class="price">€ 18,90</span></li>
    <li><h3>Surf &amp; Turf</h3><p>200g heimisches Rinderfilet<br>und Jumbo Garnelen</p><span class="price">€ 39,90</span></li>
  </ul>
  <div class="art" role="img" aria-label="Gezeichnete Grillpfanne mit Fleisch" style="left:410px;top:380px;width:170px;height:130px"></div>
  <div class="footline"></div><div class="folio">- 5 -</div>
</section>

<section class="page" style="left:35px;top:1720px">
  <div class="bracket"></div>
  <div class="art" role="img" aria-label="Gezeichnete Tomaten und Pilz" style="left:140px;top:20px;width:110px;height:60px"></div>
  <div class="title" style="left:195px;top:88px">HAUPTSPEISEN</div>
  <ul class="menu" style="left:120px;top:147px;width:340px">
    <li><h3>Wiener Schnitzel vom Schwein</h3><p>mit Pommes frites und Preiselbeeren oder mit Petersilienkartoffeln</p><span class="price">€ 18,90</span></li>
    <li><h3>Schlöfl Burger</h3><p>ca. 200g Rindfleisch mit Cheddarkäse gratiniert, Bacon, Gurken,<br>rote Zwiebel, Tomaten, Salat, serviert mit Pommes frites</p><span class="price">€ 19,50</span></li>
    <li><h3>Seeburger</h3><p>ca. 200g Rindfleisch (2 Patties) mit Cheddarkäse gratiniert, Bacon, Gurken,<br>Salat, Zwiebel-Marmelade, Tomaten, Spiegelei<br>serviert mit Saucen &amp; Pommes frites</p><span class="price">€ 24,90</span></li>
    <li><h3>Veganer Burger</h3><p>Veganes Patty / Tomate / Salat / rote Zwiebel / Wakame Alge<br>Limetten-Aioli und Pommes frites</p><span class="price">€ 18,90</span></li>
    <li><h3>Hansl's Fischsuppe</h3><p>klare Tomaten-Safransuppe mit Gemüse, verschiedenen Fischfilets,<br>Muscheln, Meeresfrüchten, Aioli - dazu Knoblauchbrot</p><span class="price">€ 22,90</span></li>
    <li><h3>Garnelen im Tontopf</h3><p>ca. 250g Black Tiger Garnelen / Knoblauch / Kräuter / bestes Olivenöl<br>hausgemachtes Aioli &amp; Brot zum Dippen</p><span class="price">€ 24,50</span></li>
  </ul>
  <div class="art square" role="img" aria-label="Gezeichneter Burger" style="left:-20px;top:350px;width:150px;height:150px"></div>
  <div class="footline"></div><div class="folio">- 6 -</div>
</section>

<section class="page" style="left:618px;top:1718px">
  <div class="title" style="left:115px;top:82px">TONI &amp; FELI EMPFEHLEN</div>
  <ul class="menu" style="left:110px;top:142px;width:330px">
    <li><h3>Feuerwehrteller „Flori" Schnitzel mit Pommes</h3><p>Kinder Brauerburger Patty vom Rind mit Cheddarkäse<br>Ketchup &amp; Pommes</p><span class="price">€ 9,90<br>€ 11,50</span></li>
    <li><h3>Chicken Sticks</h3><p>mit Pommes</p><span class="price">€ 9,90</span></li>
    <li><h3>Kater Mautz</h3><p>Mundgerechte Portion Spaghetti Bolognese</p><span class="price">€ 8,50</span></li>
    <li><h3>Räuberteller</h3><p>Leerer Teller zum Mitnaschen</p><span class="price">€ 0,00</span></li>
    <li><h3>Pommes Feli</h3><p>Portion Pommes mit Ketchup &amp; Mayo<br>...und dazu eine Fruchtsaft-Limo<br>Bubble Gum / Lemon / Peach</p><span class="price">€ 5,90<br>€ 4,50</span></li>
    <li><h3>Rotes Bergmonster</h3><p>Mundgerechte Pasta mit Tomatensauce</p><span class="price">€ 8,50</span></li>
  </ul>
  <p class="vertical-note">Alle Preise inkl. MwSt.</p>
  <div class="art" role="img" aria-label="Bunte Pizza-Figur" style="left:430px;top:20px;width:100px;height:100px"></div>
  <div class="art square" role="img" aria-label="Gezeichnete Pommes in Tüte" style="left:410px;top:340px;width:140px;height:170px"></div>
  <div class="footline"></div><div class="folio">- 7 -</div>
</section>

<section class="page" style="left:35px;top:2280px">
  <div class="bracket"></div>
  <div class="title" style="left:185px;top:82px">DESSERT</div>
  <div class="art" role="img" aria-label="Gezeichnete Beeren" style="left:310px;top:50px;width:120px;height:110px"></div>
  <ul class="menu" style="left:42px;top:143px;width:200px">
    <li><h3>Crème Brûlée</h3><p>Kirsch-Crumble &amp; Sauerrahm-Eis</p><span class="price">€ 9,90</span></li>
    <li><h3>Helles &amp; dunkles Schokoladenmousse</h3><p>mit Himbeersauce &amp; Salz-Karamell-Eis</p><span class="price">€ 9,90</span></li>
    <li><h3>Hausgemachtes Tiramisu</h3><p>italienische Rezeptur</p><span class="price">€ 8,90</span></li>
    <li><h3>Kaiserschmarrn mit Apfelmus</h3><p>Vanille- und Erdbeereis, Sahne<br>und einer kleinen Überraschung</p><span class="price">€ 14,50</span></li>
    <li><h3>Heiße Liebe</h3><p>Cremiges Vanilleeis mit heißen<br>Himbeeren und Sahne</p><span class="price">€ 8,50</span></li>
    <li><h3>Coupe Dänemark</h3><p>Vanilleeis mit heißer Schokolade<br>und Sahne</p><span class="price">€ 8,50</span></li>
    <li><h3>Gemischtes Eis</h3><p>(3 Kugeln)<br>Vanille, Erdbeer, Schokolade<br>mit oder ohne Sahne</p><span class="price">€ 7,00 / 8,40</span></li>
  </ul>
  <ul class="menu" style="left:250px;top:230px;width:190px">
    <li><h3>Schneeküss</h3><p>Vanille, Schokolade in der Schneewiese<br>mit Sprühsahne</p><span class="price">€ 7,50</span></li>
    <li><h3>Wein-Nudeln</h3><p>Tiroler Spezialität<br>Gebackene Germ-Nudel in warmem Glühwein<br>dazu leckeres Bratapfel-Eis</p><span class="price">€ 9,90</span></li>
    <li><h3>Zitronensorbet</h3><p>In der Schale serviert<br>Sahnesorbet mit Wodka</p><span class="price">€ 6,90<br>€ 8,90</span></li>
    <li><h3>Sorbet</h3><p>Vanille / Erdbeere / Galaxy</p><span class="price">€ 6,50</span></li>
  </ul>
  <div class="art square" role="img" aria-label="Gezeichnetes Tortenstück mit Beeren" style="left:-15px;top:400px;width:150px;height:120px"></div>
  <div class="footline"></div><div class="folio">- 8 -</div>
</section>

<section class="page" style="left:618px;top:2279px">
  <div class="photo" role="img" aria-label="Foto der Gaststube mit gedeckten Tischen und Panoramafenstern" style="left:110px;top:44px;width:387px;height:169px"></div>
  <div class="wordmark" style="top:232px;font-size:36px">TONI'S</div>
  <div class="photo" role="img" aria-label="Foto einer Sitznische mit Holztisch" style="left:109px;top:307px;width:155px;height:173px"></div>
  <div class="photo" role="img" aria-label="Foto des Restaurants mit Bar und Holzstühlen" style="left:272px;top:307px;width:225px;height:173px"></div>
  <div class="footline"></div><div class="folio">- 9 -</div>
</section>

<section class="page" style="left:26px;top:2845px;width:546px;height:546px">
  <div class="wordmark" style="top:128px;font-size:38px">TONI'S</div>
  <p class="contact">Bergstraße 14 · 6190 Almrosen<br>+43-5100-2874<br>info@firnblick.ag · www.almrosen.at</p>
</section>

</body>
</html>
```